Summer Fun

I need a Poster for Front of hotel advertising discounted drinks on Thursday & Fridays
$3.50.
Schooners of Local Beer, Glass of House Wine & Bubbly.
From 3.30pm to 6.30 pm
Nibblies Provided

25 + Market

Hotel

• Do not want to be known as Happy Hour.

```html
<!DOCTYPE html>
<html lang="en">
<head>
<meta charset="utf-8">
<title>Discounted Drinks Poster</title>
<link rel="stylesheet" href="https://fonts.googleapis.com/css2?family=Alfa+Slab+One&family=Oswald:wght@600;700&family=Roboto+Slab:wght@800&display=swap">
<style>
  :root {
    --frame-black: #050705;
    --slogan-green: #7dbf3c;
    --lime-light: #e6f7a4;
    --lime-mid: #9fd630;
    --lime-deep: #4f9a12;
    --maroon-dark: #4d0c10;
    --maroon: #8a1a20;
    --crimson: #b0163a;
    --crimson-dark: #7a0f26;
    --band-black: #0a0a0a;
    --white: #ffffff;
  }
  * { box-sizing: border-box; margin: 0; padding: 0; }
  html, body { width: 858px; height: 1200px; overflow: hidden; background: var(--frame-black); }
  .poster {
    position: relative; width: 858px; height: 1200px; overflow: hidden;
    background: var(--frame-black);
  }
  .slogan-strip {
    position: absolute; white-space: nowrap; overflow: hidden;
    font-family: "Oswald", sans-serif; font-weight: 600;
    font-size: 11px; letter-spacing: 0.6px; color: var(--slogan-green);
    line-height: 22px; height: 22px;
  }
  .slogan-top { left: 0; top: 0; width: 858px; }
  .slogan-bottom { left: 0; top: 1178px; width: 858px; transform: rotate(180deg); }
  .slogan-left { left: 0; top: 1200px; width: 1200px; transform-origin: 0 0; transform: rotate(-90deg); }
  .slogan-right { left: 858px; top: 0; width: 1200px; transform-origin: 0 0; transform: rotate(90deg); }

  .backdrop {
    position: absolute; left: 22px; top: 22px; width: 814px; height: 1156px;
    background:
      radial-gradient(ellipse 260px 220px at 440px 660px, var(--lime-light) 0%, rgba(230,247,164,0) 100%),
      radial-gradient(ellipse 520px 640px at 430px 600px, var(--lime-mid) 0%, var(--lime-deep) 100%);
    box-shadow: inset 0 0 40px 12px rgba(0,0,0,0.75);
  }

  .headline {
    position: absolute; left: 66px; top: 92px;
    font-family: "Alfa Slab One", serif; font-size: 62px; line-height: 89px;
    color: var(--maroon);
    background: linear-gradient(180deg, var(--maroon-dark) 0%, var(--maroon) 100%);
    -webkit-background-clip: text; background-clip: text; -webkit-text-fill-color: transparent;
    filter: drop-shadow(0 0 10px rgba(255,255,255,0.8)) drop-shadow(2px 3px 1px rgba(40,0,0,0.6));
    letter-spacing: -0.5px;
  }
  .headline span { display: block; white-space: nowrap; }

  .price-tag { position: absolute; left: 508px; top: 782px; width: 284px; height: 136px; }
  .price-tag svg { position: absolute; inset: 0; }
  .price-tag .price {
    position: absolute; inset: 0; display: flex; align-items: center; justify-content: center;
    font-family: "Oswald", sans-serif; font-weight: 700; font-size: 74px; color: var(--white);
    letter-spacing: 1px; padding-top: 6px;
  }

  .band {
    position: absolute; background: var(--band-black); color: var(--white);
    white-space: nowrap; box-shadow: 4px 6px 8px rgba(0,0,0,0.35);
  }
  .band-offer {
    left: 58px; top: 918px; width: 668px; height: 86px; transform: rotate(-1.6deg);
    font-family: "Oswald", sans-serif; font-weight: 700; font-size: 58px; line-height: 86px;
    padding-left: 42px; letter-spacing: 0.5px;
  }
  .band-days {
    left: 360px; top: 1006px; width: 442px; height: 68px; transform: rotate(-1deg);
    font-family: "Roboto Slab", serif; font-weight: 800; font-size: 40px; line-height: 66px;
    padding-left: 18px; letter-spacing: -0.5px;
  }
  .band-hours {
    left: 86px; top: 1068px; width: 500px; height: 58px; transform: rotate(-0.8deg);
    font-family: "Oswald", sans-serif; font-weight: 600; font-size: 36px; line-height: 58px;
    padding-left: 78px;
  }
</style>
</head>
<body>
<div class="poster">
  <div class="backdrop" role="img" aria-label="Lime green background with soft floating bubbles and splash texture"></div>

  <div class="slogan-strip slogan-top">YOUR SLOGAN HERE - YOUR SLOGAN HERE - YOUR SLOGAN HERE - YOUR SLOGAN HERE - YOUR SLOGAN HERE - YOUR SLOGAN HERE - YOUR SLOGAN HERE</div>
  <div class="slogan-strip slogan-right">YOUR SLOGAN HERE - YOUR SLOGAN HERE - YOUR SLOGAN HERE - YOUR SLOGAN HERE - YOUR SLOGAN HERE - YOUR SLOGAN HERE - YOUR SLOGAN HERE - YOUR SLOGAN HERE - YOUR SLOGAN HERE - YOUR SLOGAN HERE</div>
  <div class="slogan-strip slogan-bottom">YOUR SLOGAN HERE - YOUR SLOGAN HERE - YOUR SLOGAN HERE - YOUR SLOGAN HERE - YOUR SLOGAN HERE - YOUR SLOGAN HERE - YOUR SLOGAN HERE</div>
  <div class="slogan-strip slogan-left">YOUR SLOGAN HERE - YOUR SLOGAN HERE - YOUR SLOGAN HERE - YOUR SLOGAN HERE - YOUR SLOGAN HERE - YOUR SLOGAN HERE - YOUR SLOGAN HERE - YOUR SLOGAN HERE - YOUR SLOGAN HERE - YOUR SLOGAN HERE</div>

  <h1 class="headline">
    <span>Schooners</span>
    <span>of local Beer,</span>
    <span>glass of House Wine</span>
    <span>&amp; Bubbly</span>
  </h1>

  <div class="price-tag">
    <svg width="284" height="136" viewBox="0 0 284 136" aria-hidden="true">
      <defs>
        <linearGradient id="tagFill" x1="0" y1="0" x2="0" y2="1">
          <stop offset="0" stop-color="#c21a44"/>
          <stop offset="1" stop-color="#7a0f26"/>
        </linearGradient>
      </defs>
      <path d="M4 26 L280 4 L262 66 L280 132 L22 124 L36 70 Z" fill="url(#tagFill)"/>
    </svg>
    <div class="price">$3.50</div>
  </div>

  <div class="band band-offer">DISCOUNTED DRINKS</div>
  <div class="band band-days">Thursday &amp; Fridays</div>
  <div class="band band-hours">From 3.30pm to 6.30 pm</div>
</div>
</body>
</html>
```